The Logo is

Run ♪ Loud ... you can see it on the website (see below)

NB black background, font is light silver, the music character ♪ is in RED and a larger font size than the text characters.

FRONT

1. Run ♪ Loud Journal

I run an internet magazine called Run ♪ Loud Journal

www.runloudjournal.example

NB the music character ♪ is in RED and a larger font size than the text characters.

We "shoot" rock bands and then write up articles about them with photographs.

REVERSE

2. Run ♪ Loud Radio

I run a radio program called

Run ♪ Loud Radio

www.runloudjournal.example/run-loud-radio/

It's a program where we play tracks by the artists we have just seen and photographed and those that we are going to see.

3. General

It would make sense to have Run ♪ Loud Journal on one side of the card and Run ♪ Radio on the reverse.

Information on the front does not need to be repeated on the reverse but clearlt there should be a "common theme" but not necessarily a mirror effect ... as long as the Reverse side complements the Front.

I don't want to use the proforma standard Cardmill designs.

I am comfortable with wild design as this is rock n roll ... so I am not looking for geometrics or nice pastoral scenes, pretty girls or boys.

Attitude, grunt ... sweat and action ... full colour.

The words "Run Loud" may provide some opportunity for design but I have an open mind.

To get a feel for what I am looking for, I strongly suggest you have a good look around the website

www.runloudjournal.example

Finally - I'd be delighted for you to use any of my own photographs - now there's a clue - which you can see on the website - and yes, you are allowed to crop them or "distort" them if that makes sense. If you want me to send a high res image, let me know.

Good luck ...

pete harrow
editor@runloudjournal.example
+61 4 2739 5816

We are coming down to the wire ... I am very pleased with all of the submissions.  We are down to a shortlist of about 6 ... and I will provide advice over the next 24 hours or so to help you individually.  For everyone ... please note the following

The title has been standardised for both sides of the card to "Chief" ... so please change the word "Editor" or "Presenter" or "DJ" or "Publisher" to the one single title for both radio and magazine as just simply "Chief".

The email address is to be "chief@runloudjournal.example".

Any private emails please continue to send them to editor@runloudjournal.example

If you are thinking of incorporating a tag line (that would be nice) it should be

"Music With Attitude"

Thanks .. I hope that helps .... and you know, good luck.

pete

Bands, singers, performers, public relations agencies

Internet

Pete Harrow
Editor

P.O. Box 5817
East Wandilla
NSW 2189
Ph 042 739 5816

• Kamal,

Here are the two images ...

one can replace the man with his tongue out

the other can replace to main character on the other side of the card.

You can write to me directly

pete

```html
<!DOCTYPE html>
<html lang="en">
<head>
<meta charset="utf-8">
<title>Run Loud — Business Cards</title>
<link rel="stylesheet" href="https://fonts.googleapis.com/css2?family=Arimo:wght@400;700&family=Tinos&display=swap">
<style>
  :root {
    --backdrop: #e7e3dd;
    --card-black: #0b0909;
    --stage-red-dark: #2a1113;
    --stage-red: #4a1e22;
    --stage-shadow: #120c0d;
    --silver: #d9d9d9;
    --grey: #9a9a9a;
    --white: #ffffff;
    --red: #e0242c;
  }
  * { margin: 0; padding: 0; box-sizing: border-box; }
  html, body {
    width: 1200px; height: 785px; overflow: hidden;
    background: var(--backdrop);
  }
  .card-set {
    position: absolute; inset: 0;
    display: flex; align-items: center; justify-content: center; gap: 40px;
  }
  .card {
    position: relative; width: 540px; height: 309px;
    background: var(--card-black); overflow: hidden; border-radius: 3px;
    box-shadow: 0 6px 18px rgba(0,0,0,.25);
    font-family: "Arimo", Arial, sans-serif; color: var(--white);
  }
  .card__photo { position: absolute; inset: 0; }
  .card--radio .card__photo {
    background:
      radial-gradient(ellipse 40% 70% at 68% 30%, var(--stage-red) 0%, transparent 70%),
      radial-gradient(ellipse 30% 60% at 15% 40%, var(--stage-red-dark) 0%, transparent 70%),
      linear-gradient(180deg, var(--stage-shadow) 0%, var(--card-black) 100%);
  }
  .card--journal .card__photo {
    background:
      radial-gradient(ellipse 45% 55% at 58% 22%, #6a2a30 0%, transparent 70%),
      radial-gradient(ellipse 30% 70% at 22% 55%, var(--stage-red) 0%, transparent 75%),
      linear-gradient(180deg, var(--stage-red-dark) 0%, var(--stage-shadow) 70%, var(--card-black) 100%);
  }
  .card__holder {
    position: absolute; top: 14px; right: 22px; text-align: right;
    font-weight: 700; font-size: 12px; line-height: 1.25;
  }
  .card__holder-title { color: var(--red); display: block; }
  .brand {
    position: absolute; left: 0; right: 0; top: 104px;
    text-align: center;
  }
  .brand__name {
    display: inline-flex; align-items: center; gap: 12px;
    font-weight: 700; font-size: 40px; color: var(--silver);
  }
  .brand__dot {
    width: 14px; height: 14px; border-radius: 50%; background: var(--red);
  }
  .brand__label {
    display: block; margin-top: 4px;
    font-size: 13px; letter-spacing: 2px; color: var(--grey);
  }
  .accent { color: var(--red); }
  .contact {
    position: absolute; left: 26px; bottom: 56px;
    font-weight: 700; font-size: 17px; line-height: 1.3;
  }
  .card--journal .contact { bottom: 40px; font-size: 19px; }
  .tagline {
    position: absolute; left: 0; right: 0; bottom: 24px; text-align: center;
    font-size: 13px; padding-left: 150px;
  }
  .web {
    position: absolute; right: 60px; bottom: 20px;
    font-family: "Tinos", "Times New Roman", serif; font-size: 14px; color: var(--silver);
  }
</style>
</head>
<body>
  <main class="card-set">
    <article class="card card--radio">
      <div class="card__photo" role="img" aria-label="Dark concert photograph of a drummer and a guitarist on stage"></div>
      <p class="card__holder">Pete Harrow<span class="card__holder-title">Chief</span></p>
      <div class="brand">
        <span class="brand__name"><span class="brand__dot"></span>Run Loud</span>
        <span class="brand__label">RADIO</span>
      </div>
      <p class="contact">
        042 <span class="accent">739</span> 5816<br>
        <span class="accent">chief@</span>runloudjournal<span class="accent">.example</span>
      </p>
      <p class="tagline">“Music With Attitude”</p>
    </article>

    <article class="card card--journal">
      <div class="card__photo" role="img" aria-label="Red-lit concert photograph of long-haired guitarists performing"></div>
      <p class="card__holder">Pete Harrow<span class="card__holder-title">Chief</span></p>
      <div class="brand">
        <span class="brand__name"><span class="brand__dot"></span>Run Loud</span>
        <span class="brand__label">JOURNAL</span>
      </div>
      <p class="contact">
        P.O. <span class="accent">Box 5817</span> East <span class="accent">Wandilla</span><br>
        <span class="accent">NSW</span> 2189
      </p>
      <p class="web">www.runloudjournal.example</p>
    </article>
  </main>
</body>
</html>
```